create a Wedding Invitation design

Personalized wedding invitation using names, initials, a nice monogram with decorative border

incorporate names: Lena and Gordon (first names)
Holbeck (surname)
and wedding date , April 12, 2014

Colors: black ink on white;
optional accent colors: bright pink, bright orange, cajun red (may be flowers)
No shades of Purple

Industry/Entity Type

Wedding

Requirements
Must have
• Romantic, slightly formal looking design, black on white ; some accent color preferred, monogram (using first names Lena and Gordon and last name Holbeck), that could be isolated and used on RSVP cards preferred
Nice to have
• idea of being at the top of a building (venue is called Marlow Hall) - the wedding is being held on the 17th floor of building with panoramic views of Washington DC and the mountains ; Washington DC skyline, iconic DC cherry blossoms

Here are some examples of a typical Washington, DC skyline (this is an optional or secondary feature only - not to dominate the design):
http://www.pictavault.example/clip-art/washington-dc.html#comp.asp?recid=48113706&xtra=
Cherry blossoms : http://www.roamlyguide.example/news/story_8614.html

```html
<!DOCTYPE html>
<html lang="en">
<head>
<meta charset="utf-8">
<title>Lena and Gordon Holbeck – Wedding Invitation</title>
<link rel="stylesheet" href="https://fonts.googleapis.com/css2?family=Dancing+Script:wght@400;500&display=swap">
<style>
  :root {
    --paper: #ffffff;
    --edge: #efe6d6;
    --edge-deep: #e2d4bb;
    --band: #fbfaf8;
    --band-shadow: rgba(120, 100, 70, 0.28);
    --accent: #dc5a8c;
    --ink: #111111;
    --blossom-light: #f6c4d8;
    --blossom-mid: #e58bb0;
    --blossom-deep: #c85a8c;
  }
  * { margin: 0; padding: 0; box-sizing: border-box; }
  html, body {
    width: 1200px;
    height: 764px;
    overflow: hidden;
    background: var(--paper);
  }
  .invitation {
    position: relative;
    width: 1200px;
    height: 764px;
    background: var(--paper);
    box-shadow:
      inset 0 0 28px 10px var(--edge),
      inset 0 0 6px 2px var(--edge-deep);
    font-family: "Dancing Script", cursive;
  }
  .blossom-art {
    position: absolute;
    left: 375px;
    top: 90px;
    width: 450px;
    height: 250px;
  }
  .name-band {
    position: absolute;
    left: 349px;
    top: 308px;
    width: 502px;
    height: 155px;
    background: linear-gradient(180deg, #f4f1ec 0%, var(--band) 18%, var(--band) 100%);
    border-top: 1px solid #ece6dc;
  }
  .name-band::after {
    content: "";
    position: absolute;
    left: 8px;
    right: 8px;
    bottom: -2px;
    height: 6px;
    border-radius: 50%;
    box-shadow: 0 4px 8px var(--band-shadow);
  }
  .couple-names {
    position: absolute;
    left: 0;
    width: 1200px;
    top: 350px;
    text-align: center;
    font-size: 60px;
    font-weight: 400;
    color: var(--accent);
    line-height: 1;
  }
  .details {
    position: absolute;
    left: 0;
    width: 1200px;
    top: 500px;
    text-align: center;
    color: var(--ink);
    font-size: 32px;
    line-height: 50px;
  }
  .details .date { font-size: 35px; line-height: 46px; }
</style>
</head>
<body>
  <main class="invitation">
    <svg class="blossom-art" role="img" aria-label="Cluster of pink cherry blossoms on slender stems" viewBox="0 0 450 250">
      <defs>
        <radialGradient id="blossomTone" cx="50%" cy="45%" r="55%">
          <stop offset="0%" stop-color="var(--blossom-deep)"/>
          <stop offset="55%" stop-color="var(--blossom-mid)"/>
          <stop offset="100%" stop-color="var(--blossom-light)" stop-opacity="0"/>
        </radialGradient>
      </defs>
      <ellipse cx="225" cy="130" rx="225" ry="120" fill="url(#blossomTone)" opacity="0.75"/>
    </svg>

    <div class="name-band"></div>
    <h1 class="couple-names">Lena and Gordon Holbeck</h1>

    <section class="details">
      <p>request the honour of your presence at their marriage</p>
      <p class="date">April 12, 2014</p>
      <p>at half after five o'clock&nbsp; Church of St. Aldric</p>
      <p>416 Brenton Avenue&nbsp; Farrowdale, Illinois</p>
    </section>
  </main>
</body>
</html>
```